Modern, Sleek Business Card Design for Corvane Systems

Please create a modern business card, preferably all black with white logo and writing for Corvane Systems, a defense and aerospace company.

Contact Information for Business Card

symbol on one side and name, title, contact info on the other side.

```html
<!DOCTYPE html>
<html lang="en">
<head>
<meta charset="utf-8">
<title>Corvane Systems Business Card</title>
<link rel="stylesheet" href="https://fonts.googleapis.com/css2?family=Passion+One:wght@700&family=Maven+Pro:wght@500&family=PT+Serif&display=swap">
<style>
  :root {
    --page-bg: #ffffff;
    --card-bg: #1b1b1b;
    --ink: #ffffff;
  }
  html, body {
    margin: 0;
    padding: 0;
    overflow: hidden;
    background: var(--page-bg);
  }
  .canvas {
    position: relative;
    width: 1200px;
    height: 701px;
    background: var(--page-bg);
    overflow: hidden;
  }
  .card {
    position: absolute;
    background: var(--card-bg);
    border-radius: 26px;
    color: var(--ink);
  }
  .card-front {
    left: 154px;
    top: 211px;
    width: 401px;
    height: 263px;
  }
  .card-back {
    left: 660px;
    top: 204px;
    width: 411px;
    height: 273px;
  }
  .brand {
    position: absolute;
    left: 0;
    right: 0;
    top: 170px;
    display: flex;
    align-items: center;
    justify-content: center;
    gap: 12px;
  }
  .brand-mark {
    width: 14px;
    height: 14px;
    background: var(--ink);
  }
  .brand-name {
    font-family: "Maven Pro", sans-serif;
    font-weight: 500;
    font-size: 27px;
    letter-spacing: 4px;
    line-height: 1;
    color: var(--ink);
  }
  .person-name {
    position: absolute;
    left: 15px;
    top: 18px;
    margin: 0;
    font-family: "Passion One", sans-serif;
    font-weight: 700;
    font-size: 35px;
    line-height: 1;
    letter-spacing: 1.5px;
    white-space: nowrap;
  }
  .person-title {
    position: absolute;
    left: 15px;
    top: 56px;
    margin: 0;
    font-family: "Maven Pro", sans-serif;
    font-weight: 500;
    font-size: 30px;
    line-height: 1;
    white-space: nowrap;
  }
  .contact-list {
    position: absolute;
    right: 15px;
    top: 122px;
    margin: 0;
    padding: 0;
    list-style: none;
    text-align: right;
    font-family: "PT Serif", serif;
    font-size: 23px;
    line-height: 34px;
    letter-spacing: -0.8px;
    white-space: nowrap;
  }
</style>
</head>
<body>
<main class="canvas">
  <section class="card card-front" aria-label="Card front">
    <div class="brand">
      <span class="brand-mark"></span>
      <span class="brand-name">CORVANE SYSTEMS</span>
    </div>
  </section>

  <section class="card card-back" aria-label="Card back">
    <h1 class="person-name">JOHN DOE</h1>
    <p class="person-title">Program Manager</p>
    <ul class="contact-list">
      <li>john.doe@corvanesystems.com</li>
      <li>(555) 284-7190</li>
      <li>www.corvanesystems.com</li>
      <li>418 Meridian Way, Herndon, VA 20170</li>
    </ul>
  </section>
</main>
</body>
</html>
```